Attention grabbing 6x9 postcard

We are looking to have an attention grabbing post card that be sent out to homeowners from our roofing company Olum Roofing. the concept is that on the front it will say something like (STOP THE KNOCKING!
Tired of roofers knocking on your door? Contact us because we value your time as much as you value the roof over your head."
Olum Roofing
OlumRoofing.com
877.612.OLUM
info@olumroofing.com

Please feel free to come up with something very creative. Once we pick the final design we will provide the copy.

```html
<!DOCTYPE html>
<html lang="en">
<head>
<meta charset="utf-8">
<title>Olum Roofing – Stop the Knocking Postcard</title>
<link rel="stylesheet" href="https://fonts.googleapis.com/css2?family=Teko:wght@600&family=Montserrat:wght@500;800&display=swap">
<style>
  :root {
    --page-bg: #ffffff;
    --card-bg: #ffffff;
    --accent-orange: #f7941d;
    --ink: #1a1a1a;
    --photo-sky: #a9d6ec;
    --photo-roof: #4a4340;
    --photo-gable: #3c3d3b;
    --shingle-gray: #8a8888;
    --shingle-dark: #4b4a4a;
  }
  * { margin: 0; padding: 0; box-sizing: border-box; }
  html, body {
    width: 1200px; height: 1200px; overflow: hidden;
    background: var(--page-bg);
  }
  .postcard {
    position: absolute;
    left: 60px; top: 239px;
    width: 1032px; height: 690px;
    background: var(--card-bg);
    transform: scale(1.0465);
    transform-origin: top left;
    box-shadow: 0 6px 18px rgba(0,0,0,0.18);
    overflow: hidden;
  }
  .hero-photo {
    position: absolute; left: 0; top: 0;
    width: 478px; height: 690px;
    background: linear-gradient(180deg,
      var(--photo-sky) 0%, var(--photo-sky) 22%,
      var(--photo-roof) 34%, var(--photo-roof) 55%,
      #a08a60 68%, var(--photo-gable) 80%, var(--photo-gable) 100%);
  }
  .headline {
    position: absolute; left: 545px; top: 38px;
    font-family: "Teko", sans-serif; font-weight: 600;
    color: var(--accent-orange);
    font-size: 116px; line-height: 84px;
    text-transform: uppercase; letter-spacing: -1px;
    white-space: nowrap;
    transform: scaleX(0.705);
    transform-origin: left top;
  }
  .headline span { display: block; }
  .headline .indent { padding-left: 146px; }
  .shingle-swatch {
    position: absolute; left: 868px; top: 42px;
    width: 124px; height: 210px; border-radius: 10px;
    background: linear-gradient(180deg,
      var(--shingle-gray) 0%, var(--shingle-gray) 55%,
      var(--shingle-dark) 58%, var(--shingle-dark) 72%,
      var(--shingle-gray) 75%, var(--shingle-gray) 100%);
  }
  .pitch {
    position: absolute; left: 532px; top: 296px; width: 400px;
    font-family: "Montserrat", sans-serif; font-weight: 500;
    font-size: 25px; line-height: 28.7px;
    text-align: center; color: var(--ink);
  }
  .contact {
    position: absolute; left: 480px; top: 506px; width: 300px;
    font-family: "Montserrat", sans-serif; font-weight: 500; font-style: normal;
    text-align: center; color: var(--ink);
    font-size: 21.5px; line-height: 27px;
  }
  .contact .brand-word {
    display: block; font-weight: 800; font-size: 40px; line-height: 42px;
    letter-spacing: 10px; padding-left: 10px;
  }
  .contact .brand-sub { display: block; font-size: 25.5px; line-height: 30px; }
  .contact .email { font-size: 22px; }
  .mark-square {
    position: absolute; left: 854px; top: 530px;
    width: 70px; height: 70px; background: var(--ink);
  }
  .brand-name {
    position: absolute; left: 769px; top: 630px; width: 240px;
    text-align: center; white-space: nowrap;
    font-family: "Montserrat", sans-serif; font-weight: 800;
    color: var(--ink); font-size: 19px; letter-spacing: 2px;
  }
</style>
</head>
<body>
  <main class="postcard">
    <div class="hero-photo" role="img" aria-label="Roofer in a safety harness sealing shingles on a pitched roof above a gable"></div>

    <h1 class="headline">
      <span>Stop</span>
      <span class="indent">The</span>
      <span>Knocking!</span>
    </h1>

    <div class="shingle-swatch" role="img" aria-label="Close-up of weathered gray asphalt shingles"></div>

    <p class="pitch">
      Tired of roofers<br>
      knocking on your door?<br>
      Contact us because<br>
      we value your time<br>
      as much as you value<br>
      the roof over your head."
    </p>

    <address class="contact">
      <span class="brand-word">OLUM</span>
      <span class="brand-sub">ROOFING</span>
      OlumRoofing.com<br>
      877.612.OLUM<br>
      <span class="email">info@olumroofing.com</span>
    </address>

    <span class="mark-square"></span>
    <div class="brand-name">OLUM ROOFING</div>
  </main>
</body>
</html>
```